Eye catching business card

2 sided
Black background with logo in color on one side along with the words "Proudly serving the commercial and defense industries since 1975"
2nd side to contain contact information (see attached current business card) and "Waterjet, Composite, Precision Machining and Clean Room Manufacturing" with a very faint watermark of a waving USA Flag in the back ground.
Remove the "est. 195" from the current logo design

```html
<!DOCTYPE html>
<html lang="en">
<head>
<meta charset="utf-8">
<title>Northvale Machine Inc – Business Card</title>
<link rel="stylesheet" href="https://fonts.googleapis.com/css2?family=Montserrat:wght@500;600;700&family=Open+Sans:wght@400;600&display=swap">
<style>
  :root {
    --stage: #2b2c2e;
    --front-dark: #0d0e10;
    --front-mid: #1c1e22;
    --blue-brand: #1f9fe0;
    --blue-text: #1f73c6;
    --grey-text: #6f7378;
    --grey-logo: #8a8d91;
    --card-white: #ffffff;
    --flag-blue: rgba(47, 95, 170, 0.10);
    --flag-red: rgba(200, 50, 60, 0.08);
  }
  * { box-sizing: border-box; margin: 0; padding: 0; }
  html, body { width: 1200px; height: 900px; overflow: hidden; }
  body {
    background: var(--stage);
    display: flex;
    flex-direction: column;
    align-items: center;
    justify-content: center;
    gap: 40px;
    font-family: "Open Sans", sans-serif;
  }
  .card {
    width: 700px;
    height: 400px;
    position: relative;
    overflow: hidden;
  }

  /* Front */
  .card-front {
    background: radial-gradient(ellipse at 50% 40%, var(--front-mid) 0%, var(--front-dark) 75%);
    color: #fff;
    display: flex;
    flex-direction: column;
    align-items: center;
    justify-content: center;
  }
  .front-brand {
    display: flex;
    align-items: center;
    gap: 14px;
    margin-top: 10px;
  }
  .brand-square {
    width: 30px; height: 30px;
    background: var(--blue-brand);
  }
  .front-name {
    font-family: "Montserrat", sans-serif;
    font-weight: 700;
    font-size: 34px;
    letter-spacing: 1px;
    color: var(--blue-brand);
  }
  .front-rule {
    width: 340px;
    height: 2px;
    background: var(--blue-brand);
    margin-top: 14px;
  }
  .tagline {
    position: absolute;
    left: 0; right: 0;
    bottom: 36px;
    text-align: center;
    font-family: "Montserrat", sans-serif;
    font-weight: 600;
    font-size: 17px;
    letter-spacing: 0.3px;
  }

  /* Back */
  .card-back { background: var(--card-white); }
  .flag-watermark {
    position: absolute;
    right: 0; top: 0;
    width: 400px; height: 400px;
    background:
      linear-gradient(160deg, var(--flag-blue) 0%, var(--flag-blue) 35%, transparent 60%),
      linear-gradient(170deg, transparent 30%, var(--flag-red) 55%, transparent 75%, var(--flag-red) 95%);
  }
  .back-brand {
    position: absolute;
    left: 44px; top: 38px;
    font-family: "Montserrat", sans-serif;
    font-weight: 700;
    font-size: 24px;
    color: var(--grey-logo);
    letter-spacing: 0.5px;
  }
  .contact {
    position: absolute;
    left: 44px; top: 118px;
    font-size: 16px;
    color: var(--grey-text);
    line-height: 1.5;
    list-style: none;
  }
  .contact .address { margin-bottom: 8px; }
  .contact li { display: flex; align-items: center; gap: 10px; }
  .contact svg { width: 14px; height: 14px; flex: none; }
  .web-accent { color: var(--blue-text); }
  .person {
    position: absolute;
    right: 60px; top: 190px;
    text-align: right;
  }
  .person-name {
    font-family: "Montserrat", sans-serif;
    font-weight: 600;
    font-size: 30px;
    color: var(--blue-text);
    letter-spacing: 1px;
  }
  .person-title {
    font-size: 20px;
    color: var(--grey-text);
    letter-spacing: 1px;
  }
  .edge-bar {
    position: absolute;
    right: 0; top: 205px;
    width: 14px; height: 50px;
    background: var(--blue-text);
  }
  .services {
    position: absolute;
    left: 44px; right: 44px;
    bottom: 30px;
    padding-top: 14px;
    border-top: 1px solid #dfe5ec;
    font-family: "Montserrat", sans-serif;
    font-weight: 600;
    font-size: 14px;
    color: var(--blue-text);
    letter-spacing: 0.3px;
    text-align: center;
  }
</style>
</head>
<body>

<section class="card card-front">
  <div class="front-brand">
    <span class="brand-square"></span>
    <span class="front-name">NORTHVALE MACHINE INC</span>
  </div>
  <div class="front-rule"></div>
  <p class="tagline">Proudly serving the commercial and defense industries since 1975</p>
</section>

<section class="card card-back">
  <div class="flag-watermark" role="img" aria-label="Very faint waving USA flag watermark"></div>
  <div class="back-brand">NORTHVALE MACHINE INC</div>

  <ul class="contact">
    <li class="address">412 Quarry Mill Rd.<br>Glen Arden, PA 17020</li>
    <li>
      <svg viewBox="0 0 16 16" aria-hidden="true"><path d="M4 1l3 3-2 2c1 2 3 4 5 5l2-2 3 3-2 3C7 15 1 9 1 3z" fill="var(--blue-text)"/></svg>
      410-555-0142
    </li>
    <li>
      <svg viewBox="0 0 16 16" aria-hidden="true"><rect x="4" y="1" width="8" height="14" rx="1.5" fill="none" stroke="var(--blue-text)" stroke-width="1.6"/></svg>
      410-555-0187
    </li>
    <li>
      <svg viewBox="0 0 16 16" aria-hidden="true"><rect x="1" y="3" width="14" height="10" fill="none" stroke="var(--blue-text)" stroke-width="1.5"/><path d="M1 3l7 6 7-6" fill="none" stroke="var(--blue-text)" stroke-width="1.5"/></svg>
      info@northvalemachine.com
    </li>
    <li>
      <svg viewBox="0 0 16 16" aria-hidden="true"><circle cx="8" cy="8" r="6.5" fill="none" stroke="var(--blue-text)" stroke-width="1.4"/><path d="M1.5 8h13M8 1.5c-3 3.5-3 9.5 0 13M8 1.5c3 3.5 3 9.5 0 13" fill="none" stroke="var(--blue-text)" stroke-width="1.2"/></svg>
      <span>www.<span class="web-accent">northvalemachine</span>.com</span>
    </li>
  </ul>

  <div class="person">
    <div class="person-name">DALE HORNER</div>
    <div class="person-title">President</div>
  </div>
  <div class="edge-bar"></div>

  <p class="services">Waterjet, Composite, Precision Machining and Clean Room Manufacturing</p>
</section>

</body>
</html>
```